Kestrelway Advisory logo/business card design -- a digital consulting company

I've just restarted a consulting company I had years ago--Kestrelway Advisory. Now I need a new business card and updated logo. The original logo was simple enough: a chart-like progression atop a grid (see the attached file). I do strategy work, and the chart is meant to show incremental growth and profit. I'd like the reincarnation of my logo to be 3D, with both the grid and arrow rotated on their axis.

I'll want to use the logo on my website as well. I'm open to color schemes, fonts, etc.

Target Market(s)

Business-to-Business. Target market is corporate.

Industry/Entity Type

Business

Contact Information for Business Card

Logo on one-side; name and other contact info on the back

Font styles to use
Serif
Sans Serif

Requirements
Nice to have
• Kestrelway Advisory refers to the concept of "bootstrapping" or making incremental changes to grow with minimal risk and financial exposure, and self-sufficiency (think of the phrase "to pull oneself by one's bootstraps.")

```html
<!DOCTYPE html>
<html lang="en">
<head>
<meta charset="utf-8">
<title>Kestrelway Advisory – Business Card</title>
<link rel="stylesheet" href="https://fonts.googleapis.com/css2?family=Open+Sans:wght@400;700&display=swap">
<style>
  :root {
    --stage-top: #1f1f1f;
    --stage-bottom: #050505;
    --card-blue: #1f63fb;
    --card-white: #ffffff;
    --text-light: #ffffff;
    --brand-blue: #1f5ff5;
    --accent-lime: #c4d400;
  }
  * { margin: 0; padding: 0; box-sizing: border-box; }
  html, body {
    width: 1200px; height: 900px; overflow: hidden;
  }
  body {
    position: relative;
    background: linear-gradient(180deg, var(--stage-top) 0%, #141414 45%, var(--stage-bottom) 100%);
    font-family: "Open Sans", Arial, sans-serif;
  }
  .card {
    position: absolute;
    top: 306px;
    width: 440px;
    height: 271px;
    border-radius: 10px;
  }
  .card--back { left: 149px; background: var(--card-blue); color: var(--text-light); }
  .card--front { left: 608px; background: var(--card-white); }

  .back__mark {
    position: absolute;
    left: 70px; top: 92px;
    width: 90px; height: 90px;
    border-radius: 50%;
    background: var(--accent-lime);
  }
  .back__details {
    position: absolute;
    left: 224px; top: 68px;
    font-size: 12px;
    line-height: 15px;
  }
  .holder__name { font-size: 14.5px; font-weight: 700; line-height: 18px; }
  .holder__role { margin-bottom: 12px; }
  .address { margin-bottom: 12px; }
  .contact-list { list-style: none; }
  .contact-list li { display: flex; align-items: center; gap: 7px; height: 16px; }
  .contact-list svg { width: 9px; height: 9px; fill: var(--text-light); flex: none; }

  .front__brand {
    position: absolute;
    left: 0; right: 0; top: 50%;
    transform: translateY(-50%);
    display: flex; align-items: center; justify-content: center; gap: 12px;
  }
  .brand__dot {
    width: 22px; height: 22px; border-radius: 50%;
    background: var(--accent-lime);
  }
  .brand__name {
    font-size: 30px; font-weight: 400; letter-spacing: 1px;
    color: var(--brand-blue); text-transform: uppercase;
  }
</style>
</head>
<body>
  <section class="card card--back">
    <div class="back__mark" role="img" aria-label="Kestrelway Advisory brand mark area"></div>
    <div class="back__details">
      <p class="holder__name">Daniel Whitford</p>
      <p class="holder__role">Managing Director</p>
      <p class="address">12345, Address Goes Here<br>Country Name, 123456.</p>
      <ul class="contact-list">
        <li>
          <svg viewBox="0 0 10 10" aria-hidden="true"><path d="M2 0.5l1.6 2-1 1.1a6 6 0 0 0 3.8 3.8l1.1-1 2 1.6-0.9 1.6C4.5 9.6 0.4 5.5 0.4 1.4z"/></svg>
          044-987 654 321
        </li>
        <li>
          <svg viewBox="0 0 10 10" aria-hidden="true"><path d="M0.5 2h9v6h-9z M1 2.5l4 3 4-3" /></svg>
          info@kestrelway.com
        </li>
        <li>
          <svg viewBox="0 0 10 10" aria-hidden="true"><circle cx="5" cy="5" r="4.5"/></svg>
          www.kestrelway.com
        </li>
      </ul>
    </div>
  </section>

  <section class="card card--front">
    <div class="front__brand">
      <span class="brand__dot"></span>
      <span class="brand__name">Kestrelway Advisory</span>
    </div>
  </section>
</body>
</html>
```